R & T Summit Construction Business Card ideas

We want a business card to represents our company in a way that looks professional but is also a business card that is unique!

Industry/Entity Type

Construction Company

Contact Information for Business Card

open to all design ideas, just want to be able to see different options to choose from in either color or grayscale.

Requirements
Must have
• Our names and phone numbers
• Nolan Pritchett 512-804-2271
• Curtis Hale 512-693-1804
• Business logo

```html
<!DOCTYPE html>
<html lang="en">
<head>
<meta charset="utf-8">
<title>R &amp; T Summit Construction – Contact Card</title>
<link rel="stylesheet" href="https://fonts.googleapis.com/css2?family=Federo&family=Open+Sans:wght@700&display=swap">
<style>
  :root {
    --page: #ffffff;
    --frame-red: #ff0000;
    --card-white: #ffffff;
    --band-red: #b30000;
    --swoosh-pink: #f0656a;
    --swoosh-pink-light: #f7a0a3;
    --seal-red: #c40a0a;
    --seal-dark: #9a0000;
    --title-green: #0d3d0d;
    --body-grey: #333333;
  }
  html, body {
    margin: 0;
    padding: 0;
    width: 1200px;
    height: 773px;
    overflow: hidden;
    background: var(--page);
  }
  .canvas {
    position: relative;
    width: 1200px;
    height: 773px;
  }
  .card-frame {
    position: absolute;
    left: 128px;
    top: 121px;
    width: 886px;
    height: 581px;
    box-sizing: border-box;
    border: 18px solid var(--frame-red);
    background: var(--card-white);
    overflow: hidden;
  }
  .card-art {
    position: absolute;
    left: 0;
    top: 0;
    width: 850px;
    height: 545px;
  }
  .card-title {
    position: absolute;
    left: 26px;
    top: 18px;
    margin: 0;
    font-family: "Federo", serif;
    font-weight: 400;
    font-size: 42px;
    line-height: 1.2;
    color: var(--title-green);
    text-decoration: underline;
    text-decoration-thickness: 1.5px;
    text-underline-offset: 6px;
  }
  .contact-list {
    position: absolute;
    left: 10px;
    top: 283px;
    margin: 0;
    padding: 0;
    list-style: none;
    font-family: "Open Sans", sans-serif;
    font-weight: 700;
    font-size: 26px;
    line-height: 37px;
    color: var(--body-grey);
  }
  .contact-list .contact-person::before {
    content: "- ";
  }
</style>
</head>
<body>
<div class="canvas">
  <div class="card-frame">
    <svg class="card-art" viewBox="146 139 850 545" aria-hidden="true">
      <defs>
        <linearGradient id="swooshFade" x1="0" y1="0" x2="1" y2="0">
          <stop offset="0" stop-color="var(--swoosh-pink)"/>
          <stop offset="1" stop-color="var(--swoosh-pink-light)"/>
        </linearGradient>
        <radialGradient id="sealFill" cx="0.45" cy="0.4" r="0.65">
          <stop offset="0" stop-color="var(--seal-red)"/>
          <stop offset="1" stop-color="var(--seal-dark)"/>
        </radialGradient>
      </defs>
      <path class="bottom-band" d="M146,625 Q420,720 996,545 L996,684 L146,684 Z" fill="var(--band-red)"/>
      <path class="accent-swoosh" d="M146,584 Q380,650 742,574 Q400,672 146,616 Z" fill="url(#swooshFade)"/>
      <g class="approval-seal">
        <circle cx="884" cy="586" r="94" fill="var(--seal-dark)" stroke="#e9b3b3" stroke-width="2"/>
        <circle cx="884" cy="586" r="90" fill="url(#sealFill)"/>
        <circle cx="884" cy="586" r="80" fill="none" stroke="#ffffff" stroke-width="3"/>
      </g>
    </svg>
    <h1 class="card-title">Contact Information</h1>
    <ul class="contact-list">
      <li class="company-name">R &amp; T Summit Construction</li>
      <li class="contact-person">Nolan Pritchett 512-804-2271</li>
      <li class="contact-person">Curtis Hale 512-693-1804</li>
    </ul>
  </div>
</div>
</body>
</html>
```